Website for PeakStride Functional Training

We would like to launch a website for our boutique gym, PeakStride Functional Training. We'd like the website to have a lot of lime green which is one of our colors in our logo. The website will have a description of our workouts, membership, free trial class and location information.

Target Market(s)

Fitness enthusiasts, health conscious people, target ages 20-65, people looking to get fit and healthy, people looking to lose weight

Industry/Entity Type

Gym

Coding

Number of Pages Required

1 page

Font styles to use
Serif

Colors
9ccb3b
34a7d8

Requirements
Must have
• A lot of lime green to match our logo. Let the website be fun, eye catchy. Our phone number which is 614-287-9153 to be easily dialed directly from our website.
Nice to have
• We would like to include this verbiage:
• -The Most FUN 1 hour workout
• -Affordable personal training/group training
• -Individualized workout programs
• -FUN workouts delivering results
• -Turn ON fat burn-The Most FUN 1 hour workout
• -Turn ON fat burning "EPOC" after burn
• We want our website to be easily seen on smart phones, iPads, Androids
Should not have
• Font that is hard on the eyes

```html
<!DOCTYPE html>
<html lang="en">
<head>
<meta charset="utf-8">
<title>PeakStride Functional Training</title>
<link href="https://fonts.googleapis.com/css2?family=Open+Sans:wght@300;400;600;700;800&display=swap" rel="stylesheet">
<style>
:root{
  --lime:#9ccb3b;
  --blue:#34a7d8;
  --teal:#4cbfc6;
  --navy:#1b1d2e;
  --navy-deep:#15161f;
  --light:#eef0f3;
  --white:#ffffff;
  --ink:#2d2f3a;
  --muted:#8a8e9c;
  --skin:#a87a5c;
  --skin-dark:#6b4a38;
}
*{margin:0;padding:0;box-sizing:border-box}
html,body{width:1200px;height:1200px;overflow:hidden}
body{background:#e6e6e6;font-family:"Open Sans",Arial,sans-serif;position:relative}
.page{position:absolute;left:447px;top:15px;width:373px;height:1427px;transform:scale(.82);transform-origin:0 0;background:var(--navy);overflow:hidden}
.section{position:absolute;left:0;width:373px;overflow:hidden}
.abs{position:absolute}
.center{left:0;width:100%;text-align:center}
.photo{position:absolute}
.btn{position:absolute;height:11px;border-radius:6px;background:var(--lime);color:var(--white);font-size:3.6px;font-weight:700;line-height:11px;text-align:center;letter-spacing:.1px;text-decoration:none}
.btn::after{content:" \2192"}
.h-title{font-weight:700;color:var(--lime);letter-spacing:.2px}

/* header */
.hero{top:0;height:205px}
.hero-photo{inset:0;background:
  radial-gradient(ellipse 60px 45px at 175px 55px,rgba(150,150,170,.45),transparent 70%),
  radial-gradient(ellipse 40px 30px at 150px 40px,rgba(120,120,140,.35),transparent 70%),
  radial-gradient(ellipse 90px 25px at 180px 185px,rgba(70,72,88,.6),transparent 70%),
  linear-gradient(180deg,transparent 70%,rgba(8,8,14,.7) 100%),
  radial-gradient(ellipse at 45% 30%,#34374c 0%,#22243a 45%,#15161f 100%)}
.brand{position:absolute;left:31px;top:7px;color:var(--lime);font-weight:800;font-size:9px;letter-spacing:.2px}
.brand small{display:block;font-size:3.6px;font-weight:600;margin-top:-2px;letter-spacing:.3px}
.nav{position:absolute;left:117px;top:12px;display:flex;gap:9px;font-size:3.6px;color:var(--white);font-weight:600}
.social{position:absolute;left:310px;top:12px;display:flex;gap:4px}
.social span{width:4px;height:4px;border-radius:50%;background:var(--white)}
.nav-rule{position:absolute;left:0;right:0;top:27px;height:.5px;background:rgba(255,255,255,.15)}
.hero-title{top:70px;font-size:15.5px;line-height:23px;color:var(--teal)}
.hero-text{top:122px;font-size:3.8px;line-height:7px;color:#dfe2ea}

/* subscribe */
.subscribe{top:205px;height:48px}
.sub-left{left:0;top:0;width:187px;height:48px;background:var(--lime)}
.sub-right{left:187px;top:0;width:186px;height:48px;background:var(--teal)}
.sub-kicker{left:43px;top:15px;font-size:3.6px;color:var(--navy)}
.sub-head{left:43px;top:22px;font-size:11px;font-weight:800;color:var(--white)}
.sub-head b{color:var(--navy)}
.sub-input{left:200px;top:18px;width:93px;height:12px;background:var(--white);font-size:3.4px;color:var(--muted);padding:4px 4px}
.sub-btn{left:293px;top:18px;width:34px;height:12px;background:var(--lime);font-size:3.4px;color:var(--white);text-align:center;line-height:12px}

/* about */
.about{top:253px;height:164px;background:var(--light)}
.about-photo{inset:0;background:
  linear-gradient(180deg,transparent 60%,rgba(150,160,175,.35) 100%),
  linear-gradient(90deg,rgba(238,240,243,0) 30%,rgba(185,193,205,.55) 70%,rgba(160,170,185,.7) 100%),
  repeating-linear-gradient(90deg,rgba(255,255,255,.0) 0 14px,rgba(255,255,255,.5) 14px 24px),
  linear-gradient(180deg,#e4e8ee,#d3d8e0)}
.about-title{top:23px;font-size:13.5px;font-weight:300;color:var(--lime)}
.about-title b{font-weight:700}
.about-sub{top:43px;font-size:4px;font-weight:700;color:var(--ink)}
.about-text{left:75px;width:223px;font-size:3.6px;line-height:6.4px;color:#4a4d58;text-align:center}

/* shape */
.shape{top:417px;height:187px;background:var(--navy)}
.shape-photo{inset:0;background:
  radial-gradient(ellipse 28px 55px at 65px 75px,rgba(196,140,105,.85),transparent 75%),
  radial-gradient(ellipse 22px 30px at 65px 150px,rgba(45,80,130,.9),transparent 75%),
  radial-gradient(ellipse 22px 50px at 118px 95px,rgba(205,155,120,.75),transparent 75%),
  radial-gradient(ellipse 30px 40px at 160px 130px,rgba(30,32,42,.9),transparent 75%),
  radial-gradient(ellipse 120px 90px at 95px 90px,rgba(60,66,80,.9),transparent 80%),
  linear-gradient(90deg,#2b3240 0%,#262a38 55%,#1b1d2e 75%)}
.shape-title{left:190px;width:158px;top:43px;font-size:15px;line-height:21px;text-align:center}
.shape-text{left:222px;width:95px;top:91px;font-size:5.4px;line-height:9px;color:#c9ccd6;text-align:center}

/* trial band */
.trial{top:604px;height:52px;background:var(--lime)}
.trial-phone{left:65px;top:13px;font-size:8px;font-weight:800;color:var(--white);text-decoration:none}
.trial-head{left:65px;top:24px;font-size:10px;font-weight:800;color:var(--white)}
.trial-head b{color:var(--navy)}
.trial-btn{left:254px;top:19px;width:52px;height:12px;border-radius:6px;background:var(--white);color:var(--lime);font-size:3.6px;font-weight:700;text-align:center;line-height:12px}
.trial-btn::after{content:" \2192"}

/* workouts */
.workouts{top:656px;height:256px;background:var(--navy-deep)}
.wo-title{top:25px;font-size:15.5px}
.wo-cell{position:absolute;height:68px}
.wo-text{padding:9px 6px}
.wo-text h3{font-size:3.8px;font-weight:700;color:var(--white);text-transform:uppercase}
.wo-text em{display:block;font-style:normal;font-size:2.8px;color:rgba(255,255,255,.7);margin-bottom:4px}
.wo-text p{font-size:2.8px;line-height:4.4px;color:rgba(255,255,255,.75)}
.dots{display:flex;gap:1.6px;margin-top:5px}
.dots span{width:4px;height:4px;border:.4px solid rgba(255,255,255,.8);border-radius:50%}
.g{background:var(--lime)}
.t{background:var(--teal)}
.ph-a{background:radial-gradient(ellipse 26px 34px at 50% 60%,var(--skin),transparent 75%),radial-gradient(ellipse at 50% 30%,#4a4a52,#23242c)}
.ph-b{background:radial-gradient(ellipse 18px 24px at 50% 40%,#c08a6a,transparent 75%),radial-gradient(ellipse 22px 12px at 50% 70%,#c23a3a,transparent 75%),linear-gradient(135deg,#3a3a44,#1f2028)}
.ph-c{background:radial-gradient(ellipse 30px 30px at 45% 50%,#b38463,transparent 75%),linear-gradient(135deg,#2c2d36,#15161f)}
.ph-d{background:radial-gradient(ellipse 24px 30px at 50% 55%,var(--skin-dark),transparent 75%),radial-gradient(ellipse 14px 10px at 75% 40%,#3a3c46,transparent 75%),linear-gradient(135deg,#2a2b35,#17181f)}

/* stats */
.stats{top:912px;height:88px}
.stats-photo{inset:0;background:
  radial-gradient(ellipse 30px 50px at 70px 55px,rgba(150,110,90,.55),transparent 75%),
  radial-gradient(ellipse 30px 50px at 150px 60px,rgba(60,40,40,.7),transparent 75%),
  radial-gradient(ellipse 35px 55px at 255px 50px,rgba(160,110,90,.5),transparent 75%),
  linear-gradient(90deg,#5a2025 0%,#8b2f33 35%,#6e272b 65%,#3a1c20 100%)}
.stat{position:absolute;top:28px;width:40px;text-align:center;color:var(--lime)}
.stat svg{display:block;margin:0 auto 2px}
.stat strong{display:block;font-size:9px;font-weight:700;line-height:10px}
.stat span{display:block;font-size:2.8px;color:var(--white)}

/* membership */
.membership{top:1000px;height:215px;background:
  radial-gradient(ellipse 90px 60px at 30px 190px,rgba(90,200,240,.5),transparent 70%),
  radial-gradient(ellipse 90px 50px at 340px 30px,rgba(30,120,190,.5),transparent 70%),
  linear-gradient(135deg,#2f9fd4 0%,var(--blue) 45%,#2a8cc4 100%)}
.mem-title{top:18px;font-size:15.5px}
.card{position:absolute;top:48px;width:97px;height:140px;background:var(--lime);text-align:center;color:var(--white)}
.card .kind{margin-top:17px;font-size:3.4px;font-weight:600}
.card .price{font-size:12px;line-height:13px;font-weight:600}
.card .per{font-size:2.6px;margin-bottom:9px}
.card li{list-style:none;font-size:3.2px;line-height:11.5px;opacity:.9}
.card .pick{position:absolute;left:29px;top:115px;width:39px;height:8px;border-radius:4px;background:var(--teal);font-size:2.8px;line-height:8px;font-weight:700}

/* form */
.join{top:1215px;height:186px}
.join-photo{inset:0;background:
  radial-gradient(ellipse 45px 70px at 40px 90px,rgba(140,100,80,.6),transparent 75%),
  radial-gradient(ellipse 45px 70px at 320px 70px,rgba(150,110,85,.6),transparent 75%),
  linear-gradient(90deg,#3a302c 0%,#1f1e27 38%,#1f1e27 62%,#4a3a33 100%)}
.join-title{top:27px;font-size:15.5px}
.join-text{left:112px;width:149px;top:47px;font-size:3.4px;line-height:5.6px;color:#d4d6de;text-align:center}
.field{position:absolute;left:111px;width:151px;background:var(--white);font-size:3.2px;color:var(--muted);padding:2.5px 4px}

/* footer */
.footer{top:1401px;height:26px;background:var(--lime)}
.footer .brand{top:3px;color:var(--white)}
.copy{position:absolute;right:31px;top:11px;font-size:2.8px;color:var(--white)}
</style>
</head>
<body>
<main class="page">

  <header class="section hero">
    <div class="photo hero-photo" role="img" aria-label="Athlete lifting weights in a dark gym"></div>
    <div class="brand">PEAKSTRIDE<small>Functional Training</small></div>
    <nav class="nav"><span>HOME</span><span>ABOUT US</span><span>SERVICES</span><span>GALLERY</span><span>TEAM</span><span>CONTACT</span></nav>
    <div class="social"><span></span><span></span><span></span><span></span></div>
    <div class="nav-rule"></div>
    <h1 class="abs center h-title hero-title">WINTER SPECIAL OFFER<br>GET 30% ON ALL PROGRAM</h1>
    <p class="abs center hero-text">Lorem Ipsum is simply dummy text of the printing and typesetting industry.<br>Lorem Ipsum has been the industry's standard dummy text.</p>
    <a class="btn" style="left:160px;top:157px;width:53px">JOIN PROGRAM</a>
  </header>

  <section class="section subscribe">
    <div class="abs sub-left"></div>
    <div class="abs sub-right"></div>
    <div class="abs sub-kicker">SUBSCRIBE <span style="color:#fff">NOW</span></div>
    <div class="abs sub-head">DISCOUNT <b>20%!</b></div>
    <div class="abs sub-input">Enter Email</div>
    <div class="abs sub-btn">SEND</div>
  </section>

  <section class="section about">
    <div class="photo about-photo" role="img" aria-label="Bright gym floor with training machines"></div>
    <h2 class="abs center about-title">ABOUT <b>PEAKSTRIDE GYM</b></h2>
    <p class="abs center about-sub">Lorem Ipsum is simply dummy text of the printing and typesetting industry.</p>
    <p class="abs about-text" style="top:57px">Lorem Ipsum is simply dummy text of the printing and typesetting industry. Lorem Ipsum has been the industry's standard dummy text ever since the 1500s, when an unknown printer took a galley of type and scrambled it to make a type specimen book.</p>
    <p class="abs about-text" style="top:83px">Lorem Ipsum is simply dummy text of the printing and typesetting industry. Lorem Ipsum has been the industry's standard dummy text ever since the 1500s, when an unknown printer took a galley of type and scrambled it to make a type specimen book.</p>
    <a class="btn" style="left:160px;top:124px;width:53px">JOIN PROGRAM</a>
  </section>

  <section class="section shape">
    <div class="photo shape-photo" role="img" aria-label="Muscular man and woman posing on a gym bench"></div>
    <h2 class="abs h-title shape-title">THE PLACE TO<br>GET IN SHAPE</h2>
    <p class="abs shape-text">For fitness and workout, we are available for 24/7 for your fitness.</p>
    <a class="btn" style="left:244px;top:129px;width:53px">JOIN PROGRAM</a>
  </section>

  <section class="section trial">
    <a class="abs trial-phone" href="tel:+16142879153">614-287-9153</a>
    <div class="abs trial-head">FREE <b>TRIAL CLASS</b></div>
    <a class="abs trial-btn">JOIN PROGRAM</a>
  </section>

  <section class="section workouts">
    <h2 class="abs center h-title wo-title">WORKOUT OF THE DAY</h2>
    <div class="wo-cell ph-a" style="left:31px;top:59px;width:68px" role="img" aria-label="Man shouting during a workout"></div>
    <div class="wo-cell g wo-text" style="left:99px;top:59px;width:87px"><h3>The Most Fun</h3><em>1 hour workout</em><p>Lorem ipsum is simply dummy text of the printing and typesetting industry, made to fill space.</p><div class="dots"><span></span><span></span><span></span></div></div>
    <div class="wo-cell ph-b" style="left:186px;top:59px;width:69px" role="img" aria-label="Woman flexing her arms"></div>
    <div class="wo-cell t wo-text" style="left:255px;top:59px;width:87px"><h3>Personal Training</h3><em>Group training</em><p>Lorem ipsum is simply dummy text of the printing and typesetting industry, made to fill space.</p><div class="dots"><span></span><span></span><span></span></div></div>
    <div class="wo-cell ph-c" style="left:31px;top:127px;width:68px" role="img" aria-label="Athlete posing with muscles flexed"></div>
    <div class="wo-cell t wo-text" style="left:99px;top:127px;width:87px"><h3>Individualized Workout</h3><em>Programs</em><p>Lorem ipsum is simply dummy text of the printing and typesetting industry, made to fill space.</p><div class="dots"><span></span><span></span><span></span></div></div>
    <div class="wo-cell ph-d" style="left:186px;top:127px;width:69px" role="img" aria-label="Man lifting a dumbbell"></div>
    <div class="wo-cell g wo-text" style="left:255px;top:127px;width:87px"><h3>Fun &amp; Delivering Results</h3><em>Workouts</em><p>Lorem ipsum is simply dummy text of the printing and typesetting industry, made to fill space.</p><div class="dots"><span></span><span></span><span></span></div></div>
    <a class="btn" style="left:160px;top:216px;width:53px">JOIN PROGRAM</a>
  </section>

  <section class="section stats">
    <div class="photo stats-photo" role="img" aria-label="Group of athletes training together"></div>
    <div class="stat" style="left:51px"><svg width="9" height="8" viewBox="0 0 9 8"><rect x=".5" y=".5" width="8" height="7" fill="none" stroke="#9ccb3b" stroke-width=".8"/><path d="M2 5 4 3 6 5" fill="none" stroke="#9ccb3b" stroke-width=".8"/></svg><strong>985</strong><span>MEMBERS</span></div>
    <div class="stat" style="left:128px"><svg width="9" height="8" viewBox="0 0 9 8"><path d="M4.5 7.3 1 4A2 2 0 0 1 4.5 1.4 2 2 0 0 1 8 4Z" fill="none" stroke="#9ccb3b" stroke-width=".8"/></svg><strong>86</strong><span>TRAINERS</span></div>
    <div class="stat" style="left:205px"><svg width="9" height="8" viewBox="0 0 9 8"><path d="M.5 1h3.5v6H.5ZM5 1h3.5v6H5Z" fill="none" stroke="#9ccb3b" stroke-width=".8"/></svg><strong>58</strong><span>CLASSES</span></div>
    <div class="stat" style="left:282px"><svg width="9" height="8" viewBox="0 0 9 8"><path d="M1.5 6V4a3 3 0 0 1 6 0v2" fill="none" stroke="#9ccb3b" stroke-width=".8"/><rect x="1" y="5" width="2" height="2.5" fill="#9ccb3b"/><rect x="6" y="5" width="2" height="2.5" fill="#9ccb3b"/></svg><strong>46</strong><span>PROGRAMS</span></div>
  </section>

  <section class="section membership">
    <h2 class="abs center h-title mem-title">EFFECTIVE MEMBERSHIP</h2>
    <div class="card" style="left:31px"><div class="kind">PERSONAL</div><div class="price">$95</div><div class="per">ONE MONTH</div><ul><li>Swimming pool not included</li><li>Content optional</li><li>Towels not included</li><li>Water not included</li><li>Personal trainer not included</li></ul><div class="pick">CHOOSE PLAN</div></div>
    <div class="card" style="left:137px"><div class="kind">PERSONAL</div><div class="price">$499</div><div class="per">SIX MONTHS</div><ul><li>Swimming pool + $10</li><li>Content optional</li><li>Towels for FREE</li><li>Water + $3</li><li>Personal trainer optional</li></ul><div class="pick">CHOOSE PLAN</div></div>
    <div class="card" style="left:244px"><div class="kind">PERSONAL</div><div class="price">$999</div><div class="per">ONE YEAR</div><ul><li>Swimming pool for FREE</li><li>Content included</li><li>Towels for FREE</li><li>Water for FREE</li><li>Personal trainer included</li></ul><div class="pick">CHOOSE PLAN</div></div>
  </section>

  <section class="section join">
    <div class="photo join-photo" role="img" aria-label="Smiling members resting in the gym"></div>
    <h2 class="abs center h-title join-title">1 DAY FREE TRIAL</h2>
    <p class="abs join-text">Lorem Ipsum is simply dummy text of the printing and typesetting industry. Lorem Ipsum has been the industry's standard dummy text ever since the 1500s, when an unknown printer took a galley of type.</p>
    <div class="field" style="top:77px;height:10px">Your Name</div>
    <div class="field" style="top:94px;height:10px">Your Email</div>
    <div class="field" style="top:111px;height:29px">Your Message</div>
    <a class="btn" style="left:163px;top:148px;width:47px">SEND MESSAGE</a>
  </section>

  <footer class="section footer">
    <div class="brand">PEAKSTRIDE<small>Functional Training</small></div>
    <div class="copy">&copy; 2017 All Rights Reserved by PEAKSTRIDE</div>
  </footer>

</main>
</body>
</html>
```